Webdesign for recipe site

Please take a look at www.pfannenwelt.com. PW is a community site with around 60000 user recipes. It is a one-man-project and needs a redesign.
The new design shall meet these facts
high usability
1st focus on content
2nd focus on search and registration-elements
flat menü ? much content above the fold
well contured font type, size and color
coherent button, box and element design
useful design guide for the whole site
flexible font-sizes (changable css)
flexible color set for day and night mode (changable css)
And these facts shall not change
Keeping the „soul“ of pfannenwelt. PW is an independent and free recipe source. No media corporation. Everyone can participate.
This means, that PW is seen as a very personal, even private website and the design shall transport this. The design shall not be cold or heartless. It shall work and leave a cheerful impression as well. The design shall keep the atmosphere of a one-man-project, where everyone is welcomed and the personal touch is warm and heartly.
Since 8 years, the major color is red. The tone must be kept while the intensitity shall be lowered. A decent background and a warm and welltought color set are wanted in a way, that the tone of the website is still seen as red. Probably the links shall remain red, that way the rest can be set less intense.
And these facts are open
The design elements are the cook and the red tomato. While it would be nice to keep the cook (not required at any means), the tomato could be dropped. If they fit into a new design – great, if not, it's ok.
Example Pages
Recipe: http://www.pfannenwelt.com/r/68765-panini-vereinfachte-variation.html
Category: http://www.pfannenwelt.com/kb/0k0/Backrezept/rezepte.html
Homepage: http://www.pfannenwelt.com
Updates
A nice color set: http://www.artfolkhub.com/design/463831
A well structured design: http://www.artfolkhub.com/design/452858
Reason: Just 3 days left and no submission yet.
We will guarantee the project payment (thanks for hinting, Tomas) and extend the deadline by 7 days.
Thank you for your submissions.
The brown/red/beige color-sets are good, they lead the way. The layout though is mostly too playful. It shall be clean and simple and likely to fit for all the content, for the single recipe as well as the recipe lists, the profile page and the homepage.
I got inspired by you color sets and set up a testpage that pretty much goes in to the direction I want. Very flat header, peaceful and warm colors, no distraction, focus on the content. What's still missing is the breadcrumb section and an idea to fill the homepage and the recipe lists. And probably the colors (especially the light background-color, is it beige?) can also be better choosen.
Please see http://www.pfannenwelt.com/test-543677423/r_v01.html
Kind regards, Lukas
Reason: I extend the deadline once more to give Wurl Studio the opportunity to participate. It would be nice to see drafts that go more into the clean and simple direction as I updated in the brief. Here is the current status: http://www.pfannenwelt.com/r/60262-steak-auf-spargel.html (is on test now). Maybe the beige-colors can be choosen more cleaner and suggestions for the homepage and recipe lists and the footer are very welcome also. Looking forward for your designs!
I'll put the Feedback on the latest design of quietmaple in the brief, so you all find it.
http://www.artfolkhub.com/design/587249/web-design-by-quietmaple
-
Dont't know man, this still doesn't look as clean as I need it. There are 100s of recipe sites online and it is urgent to design the page with clear focus on the content. As little distraction as possible, there will be ads for that.
Mainly, you did too much. There are too many design elements and the round bites with the squares. The header shall be as small as in the mentioned page: http://www.pfannenwelt.com/r/60262-steak-auf-spargel.html
I show you an example of a clean page as I see it: http://www.rankvilo.org/q/ips-and-domains
These are not the colors I want but they all fit together. I also need the font larger and the basic color scheme must be warmer. But maybe you can understand where I'm going or where I want to go.
Please do it very simple, with no corners, as flat and clean as possible, with a genuine feeling on first site of where the content is, what the focus of the site is (content).
Thank's.
Target Market(s)
age 35-55, majority is female, interested in recipes, cooking, baking
Industry/Entity Type
Media
Look and feel

```html
<!DOCTYPE html>
<html lang="de">
<head>
<meta charset="utf-8">
<title>Pfannenwelt – Rezepte tauschen</title>
<link href="https://fonts.googleapis.com/css2?family=PT+Sans:wght@400;700&family=Arimo:wght@400;700&display=swap" rel="stylesheet">
<style>
:root{
  --page:#7e0505;
  --nav-top:#e32a22;
  --nav-bottom:#b30d0d;
  --nav-active:#e8362b;
  --brown:#3c1d10;
  --brown-mid:#4c2414;
  --cream:#faf2e1;
  --cream-light:#fdf9f0;
  --line:#9c7b68;
  --red:#a3100e;
  --link:#d3150f;
  --text:#2b1d16;
  --orange:#c2551e;
}
*{margin:0;padding:0;box-sizing:border-box}
html,body{width:939px;height:1200px;overflow:hidden;background:var(--page)}
body{position:relative;font-family:"Arimo",Arial,sans-serif;color:var(--text)}
.abs{position:absolute}
a{color:inherit;text-decoration:none}

.toplinks{left:700px;top:23px;color:#fff;font:700 11px "PT Sans",sans-serif;letter-spacing:.3px}
.toplinks span{margin:0 6px}

.nav{left:43px;top:41px;width:853px;height:48px;border-radius:12px 12px 0 0;background:linear-gradient(var(--nav-top),var(--nav-bottom));display:flex;overflow:hidden}
.nav a{color:#fff;font:700 13px "PT Sans",sans-serif;padding:0 17px;line-height:44px;border-right:2px dotted #f3b3a8;height:44px;margin-top:0}
.nav a:last-child{border-right:none}
.nav a.active{background:var(--nav-active);padding:0 16px 0 25px}

.header{left:43px;top:89px;width:853px;height:244px;background:var(--brown)}
.brand{left:47px;top:93px;width:283px;height:165px;background:var(--cream-light);display:flex;align-items:center;justify-content:center;gap:8px}
.brand .dot{width:14px;height:14px;border-radius:50%;background:var(--red)}
.brand .name{font:700 34px "PT Sans",sans-serif;color:var(--red)}
.search-tabs{left:59px;top:268px;color:#fff;font:700 13px "PT Sans",sans-serif}
.search-tabs span{margin:0 6px}
.search-input{left:59px;top:296px;width:159px;height:24px;background:var(--brown);border:1px solid #9a8070}
.search-btn{left:231px;top:293px;width:90px;height:28px;border-radius:3px;background:linear-gradient(#fff,#eadfce);color:var(--red);font:700 14px "PT Sans",sans-serif;text-align:center;line-height:28px}
.hero{left:330px;top:93px;width:562px;height:236px;background:linear-gradient(135deg,#e7d6b3 0%,#c43524 35%,#4a6a2c 60%,#d1362a 80%,#e9dcc2 100%)}

.content{left:43px;top:333px;width:853px;height:824px;background:var(--cream);border-radius:0 0 12px 12px}

.box{position:absolute;left:49px;width:216px;border:1px solid var(--line);border-radius:10px;background:var(--cream)}
.box h3{font:700 15px "PT Sans",sans-serif;color:var(--red);padding:6px 0 0 18px;height:32px;border-bottom:1px solid var(--line)}
.box ul{list-style:none;padding:8px 0 0 24px}
.box li{font-size:11.5px;line-height:20.5px;padding-left:10px;position:relative}
.box li::before{content:"";position:absolute;left:0;top:7px;border-left:5px solid var(--text);border-top:3.5px solid transparent;border-bottom:3.5px solid transparent}
.more{position:absolute;color:var(--link);font:700 11.5px "PT Sans",sans-serif}
.more svg{vertical-align:-1px;margin-left:4px}

.tags{left:56px;top:941px;width:201px;height:139px;border:1px solid var(--line);padding:22px 12px 0 12px;line-height:14px;color:var(--red)}
.tags a{text-decoration:underline;font-weight:700;margin-right:4px}
.t1{font-size:9.5px}.t2{font-size:13px}.t3{font-size:11px}.t4{font-size:14px}
.follow{left:72px;top:1089px;font:400 15px "PT Sans",sans-serif;color:var(--text)}
.social{top:1117px;width:21px;height:21px;border-radius:50%;background:#3f7ab8;border:2px solid #cfe0f0}

.h1{left:286px;top:355px;font:700 21px "PT Sans",sans-serif;color:var(--red);letter-spacing:.3px}
.intro{left:287px;top:387px;width:605px;font-size:12.2px;line-height:15.5px;text-align:justify;color:var(--text)}
.btn{top:444px;width:134px;height:21px;background:var(--brown-mid);border-radius:3px;color:#fff;font:700 12.5px "PT Sans",sans-serif;padding-left:8px;line-height:21px}
.dots{height:0;border-top:2px dotted #6b4a38}

.h2{font:700 15px "PT Sans",sans-serif;color:var(--red);letter-spacing:.2px}
.thumb{top:530px;width:86px;height:64px;border:2px solid var(--brown)}
.cap{top:608px;font:700 10.5px "PT Sans",sans-serif;line-height:12px;color:var(--text)}
.pill{position:absolute;width:57px;height:16px;background:var(--link);border-radius:3px;color:#fff;font:700 10.5px "PT Sans",sans-serif;padding-left:9px;line-height:16px;box-shadow:1px 1px 0 #7a1a0f}

.knodel-img{left:285px;top:695px;width:171px;height:136px;border:2px solid var(--brown);background:radial-gradient(circle at 45% 60%,#efe4c2 0 28%,#9ab35a 40%,#e45a2e 52%,#7c6a52 75%)}
.klist{left:484px;top:728px;font:700 12px "PT Sans",sans-serif;line-height:24px;color:var(--text);letter-spacing:.2px}
.kpara{left:291px;top:884px;width:369px;font-size:11px;line-height:13.8px;text-align:justify}

.mag-img{left:295px;width:70px;height:51px;border:2px solid var(--brown)}
.mag-title{left:378px;font:700 13.5px "PT Sans",sans-serif;color:var(--link)}
.mag-text{left:378px;width:283px;font:700 11.8px "PT Sans",sans-serif;line-height:15.5px;color:var(--text);letter-spacing:.2px}

.comments{left:691px;top:495px;width:199px;height:547px;border:1px solid var(--line);background:var(--cream)}
.comments h3{font:700 15px "PT Sans",sans-serif;color:var(--red);padding:13px 0 0 20px;height:37px;border-bottom:1px solid var(--line)}
.cm{position:absolute;left:10px;width:178px}
.cm .who{font-size:11px;line-height:13px;color:var(--red);text-align:justify}
.cm .txt{font-size:10px;line-height:12px;margin-top:12px;text-align:justify}

.newsletter{left:691px;top:1055px;width:199px;height:87px;background:var(--brown)}
.newsletter .t{position:absolute;left:18px;top:7px;color:#fff;font:400 15px "PT Sans",sans-serif}
.newsletter .in{position:absolute;left:14px;top:30px;width:176px;height:23px;background:#fff}
.newsletter .sub{position:absolute;left:57px;top:61px;width:70px;height:23px;background:var(--orange);border-radius:3px;color:#fff;text-align:center;font:700 12px "PT Sans",sans-serif;line-height:23px}

.footer{left:58px;top:1168px;color:#fff;font-size:10.5px;line-height:15.5px;letter-spacing:.3px}
.footer span{margin:0 4px}
</style>
</head>
<body>

<div class="abs toplinks"><a href="#">Login</a><span>|</span><a href="#">Kostenlos Registrieren</a></div>

<nav class="abs nav">
  <a class="active" href="#">Start</a><a href="#">Rezepte</a><a href="#">Magazin</a><a href="#">Foren</a><a href="#">Gemeinschaft</a><a href="#">Markt</a>
</nav>

<div class="abs header"></div>
<div class="abs brand"><span class="dot"></span><span class="name">Pfannenwelt</span></div>
<div class="abs search-tabs">Rezepte<span>|</span>Mitglieder<span>|</span>den Foren</div>
<div class="abs search-input"></div>
<div class="abs search-btn">Search</div>
<div class="abs hero" role="img" aria-label="Foto: Tomaten mit Basilikum, Rosmarin und Pesto"></div>

<div class="abs content"></div>

<!-- left column -->
<div class="box" style="top:354px;height:188px">
  <h3>New Rezepte</h3>
  <ul><li>Sacher-Schnitten</li><li>Bananan-Apfel-Kuchen</li><li>Knautschballen</li><li>Frittfisch</li><li>Leckerer Thunfischaufstrich</li></ul>
</div>
<a class="more" style="left:187px;top:510px" href="#">more<svg width="11" height="10"><path d="M0 0L11 5L0 10L3 5Z" fill="#d3150f"/></svg></a>

<div class="box" style="top:551px;height:186px">
  <h3>Aktuelle Saisonrezepte</h3>
  <ul><li>Sacher-Schnitten</li><li>Bananan-Apfel-Kuchen</li><li>Knautschballen</li><li>Frittfisch</li><li>Leckerer Thunfischaufstrich</li></ul>
</div>
<a class="more" style="left:187px;top:712px" href="#">more<svg width="11" height="10"><path d="M0 0L11 5L0 10L3 5Z" fill="#d3150f"/></svg></a>

<div class="box" style="top:745px;height:188px">
  <h3>Aktuell in den Foren</h3>
  <ul><li>Neues Spiel: Ahnungen</li><li>Rezept Haller Hackgedöns</li><li>ein kleines Spiel...</li><li>Lebensweisheiten</li><li>Was kocht Ihr denn heute?</li></ul>
</div>
<a class="more" style="left:65px;top:906px" href="#">weitere aktuelle Forenbeiträge<svg width="11" height="10"><path d="M0 0L11 5L0 10L3 5Z" fill="#d3150f"/></svg></a>

<div class="abs tags">
  <a class="t1">Sprossengemüse</a> <a class="t4">Gemüse und</a> <a class="t4">Obst</a> <a class="t3">Aufläufe und Souffles</a> <a class="t2">Abendessen</a> <a class="t1">Frühling</a> <a class="t2">Rind</a> <a class="t1">Steak</a> <a class="t1">Spargel</a> <a class="t1">Fleischgerichte</a> <a class="t1">überbacken</a> <a class="t4">Hauptgerichte</a> <a class="t4">Fleisch</a> <a class="t1">Überbackenes</a> <a class="t1">gratinieren</a>
</div>
<div class="abs follow">Follow us</div>
<div class="abs social" style="left:80px"></div>
<div class="abs social" style="left:106px"></div>

<!-- main -->
<h1 class="abs h1">Rezepte tauschen? Pfannenwelt!</h1>
<p class="abs intro">Du liebst gute Rezepte? Willkommen bei Pfannenwelt. Hier findest du tausende Rezepte, viele mit Bild. Du kannst jedes Rezept speichern und kommentieren. Und du kannst sofort deine eigenen Rezepte und Bilder hochladen. Ohne Wartezeiten. Los geht's.</p>
<a class="abs btn" style="left:278px" href="#">Registrieren →</a>
<a class="abs btn" style="left:420px" href="#">Rezepte finden →</a>
<a class="abs btn" style="left:562px" href="#">Rezept eintragen →</a>
<div class="abs dots" style="left:275px;top:485px;width:613px"></div>

<h2 class="abs h2" style="left:288px;top:495px">Das Beste vom Tage</h2>
<div class="abs thumb" style="left:288px;background:linear-gradient(#e8742a,#c9a06a)" role="img" aria-label="Foto: Torte mit Mandarinen"></div>
<div class="abs thumb" style="left:388px;background:radial-gradient(circle,#6e2216 25%,#f0e8dc 45%,#c9b89a)" role="img" aria-label="Foto: Dessert im Teller"></div>
<div class="abs thumb" style="left:489px;background:linear-gradient(#d04a25,#f2e4c8 40%,#e9a43a 70%,#ddd)" role="img" aria-label="Foto: Waffel-Schnitte"></div>
<div class="abs thumb" style="left:590px;background:linear-gradient(#d04a25,#f2e4c8 40%,#e9a43a 70%,#ddd)" role="img" aria-label="Foto: Mousse-Schnitte"></div>
<div class="abs cap" style="left:293px">Filetpfanne mit<br>Speckbohnen</div>
<div class="abs cap" style="left:390px">Österreichischer<br>Kaiserschmarrn</div>
<div class="abs cap" style="left:493px;top:605px">Waffel-<br>Grundrezept</div>
<div class="abs cap" style="left:598px;top:605px">Mousse&nbsp;&nbsp;&nbsp;au<br>chocolat</div>
<a class="pill" style="left:610px;top:647px" href="#">more ➡</a>
<div class="abs dots" style="left:273px;top:673px;width:407px"></div>

<div class="abs knodel-img" role="img" aria-label="Foto: Semmelknödel mit Salat"></div>
<h2 class="abs h2" style="left:475px;top:693px">Knödel - eine runde Sache</h2>
<div class="abs klist">&gt; Fleischknödel<br>&gt; Topfenknödel<br>&gt; Waldviertler-Knödel<br>&gt; Tschechische Hefeknödel<br>ohne Semmel<br>&gt; Brotknödel mit Schokolade</div>
<p class="abs kpara">Wissenswertes über Knödel, Buchtipps, Rezepte, außerdem alle Rezepte mit dem Schlagwort Knödel (357) und die Knödelei in der Rezeptbox von Sr.Margarete</p>
<a class="pill" style="left:605px;top:925px" href="#">more ➡</a>
<div class="abs dots" style="left:275px;top:962px;width:407px"></div>

<h2 class="abs h2" style="left:289px;top:979px">Neu im Magazin</h2>
<div class="abs mag-img" style="top:1009px;background:radial-gradient(circle at 40% 50%,#d98a8a 30%,#7a5a4a 60%,#ccc)" role="img" aria-label="Foto: Pitahaya-Früchte"></div>
<div class="abs mag-title" style="top:1005px">Silvester</div>
<div class="abs mag-text" style="top:1026px">Ab Mitte Dezember gibt es in den Supermärkten bei den Exoten wieder Pitahayas. Was ist das eigentlich für eine Frucht?</div>
<div class="abs mag-img" style="top:1088px;background:radial-gradient(circle,#b9a48a 30%,#7a3b2e 55%,#4a2a20)" role="img" aria-label="Foto: aufgeschnittene Pitahaya"></div>
<div class="abs mag-title" style="top:1088px">Pitahaya - was ist das nun wieder?</div>
<div class="abs mag-text" style="top:1109px">Allerlei Infos zum Jahreswechsel.</div>

<!-- right column -->
<div class="abs comments">
  <h3>Aktuelle Kommentare</h3>
  <div class="cm" style="top:55px"><div class="who">kuchenbacke zu Semmelknödel aus dem Backofen</div><div class="txt" style="padding-left:3px">Das sollte doch auch mit Backpapier gehen, dann kann man das Fett auch noch weglassen. Auf jeden Fall werd ich die mal probieren, könnten prima zu meinen Putenrouladen passen.</div></div>
  <div class="cm" style="top:187px"><div class="who">hw zu Semmelknödel aus dem Backofen</div><div class="txt">Das ist ja eine klasse Idee - villt. krieg ich ja auf diesem Weg meinen GG zum Semmelknödel essen</div></div>
  <div class="cm" style="top:292px"><div class="who">Almdirndl zu Bunter Tortellinisalat</div><div class="txt" style="margin-top:15px">klasse Idee, mal was anderes .</div></div>
  <div class="cm" style="top:365px"><div class="who">Almdirndl zu Bunter Tortellinisalat</div><div class="txt" style="margin-top:15px">klasse Idee, mal was anderes .</div></div>
  <div class="cm" style="top:441px"><div class="who">Almdirndl zu Bunter Tortellinisalat</div><div class="txt" style="margin-top:17px">klasse Idee, mal was anderes .</div></div>
</div>
<a class="more" style="left:725px;top:1008px;font-size:12px" href="#">weitere Kommentare<svg width="11" height="10"><path d="M0 0L11 5L0 10L3 5Z" fill="#d3150f"/></svg></a>

<div class="abs newsletter">
  <div class="t">Sign up for Newsletter</div>
  <div class="in"></div>
  <div class="sub">Submit</div>
</div>

<div class="abs footer">Impressum<span>|</span>Kontakt<span>|</span>Team<span>|</span>Urheberrecht<span>|</span>AGB<span>|</span>Regeln<span>|</span>Hier werben<span>|</span>Stats<span>|</span>Externe Nutzung<br>RSS: Rezept des Tages<span>|</span>RSS: Neue Rezepte</div>

</body>
</html>
```